Natural Stone Company Redesign

Looking for a fresh, creative, website design. We service Luxury Residential projects in US and Internationally. We would like to see a design that communicates a passion for creative challenging design that is merged with natural stone projects. Our new company Logo is "Inspiration meets Earth"

We like to emphasis from concept to completion, for example, photos of blueprints and/or sketches of a project, then a completion photo of same project.

some websites we like are:
http://www.brelmofask.com/
http://tovanquistdesign.com/

We would like to highlight our services of "concept to completion" scenario. Blueprints/sketches to finished products.
Page needed:
Home
About Us
Projects
Contact Us

Target Market(s)

Developers, architects, designers

Industry/Entity Type

It Company

Number of Pages Required

4 page

Font styles to use
Sans Serif

Requirements
Must have
• "Inspiration Meets Earth"
• New, innovative, look.
• Something to grab the attention, and make them think
Nice to have
• Motion on the homepage
• Roll over the finished project photo, and have the name of the stone pop up

```html
<!DOCTYPE html>
<html lang="en">
<head>
<meta charset="utf-8">
<title>KORA — Contact Us</title>
<link rel="stylesheet" href="https://fonts.googleapis.com/css2?family=Crimson+Text:wght@400&family=Roboto:wght@300;400;500&display=swap">
<style>
:root{
  --green:#6db33f;
  --green-soft:#8cc866;
  --ink:#222222;
  --text:#555555;
  --muted:#888888;
  --line:#e6e6e6;
  --footer:#2b2b2b;
  --footer-bottom:#222222;
  --white:#ffffff;
}
*{box-sizing:border-box;margin:0;padding:0}
html,body{width:714px;height:1200px;overflow:hidden;background:var(--white)}
body{position:relative;font-family:"Roboto",sans-serif;color:var(--text)}
h1,h2,h3,h4{font-weight:400}
.abs{position:absolute}

/* Hero */
.hero{left:0;top:0;width:714px;height:308px;
  background:linear-gradient(180deg,#3f7fc9 0%,#7aa6d6 28%,#c9b59c 52%,#8a6f5a 74%,#5d4a3f 100%)}
.hero-shade{left:0;top:0;width:714px;height:308px;background:rgba(0,0,0,.18)}
.brand{left:0;top:0;width:58px;height:37px;background:#2a2a2a;color:var(--white);
  font-family:"Crimson Text",serif;font-size:14px;line-height:37px;text-align:center;letter-spacing:.5px}
.nav a{position:absolute;top:23px;color:var(--white);font-size:7.5px;text-decoration:none}
.nav .btn{top:18px;left:570px;width:66px;height:20px;border-radius:10px;background:var(--green);
  text-align:center;line-height:20px}
.burger{left:649px;top:23px}
.hero-title{left:0;width:714px;top:204px;text-align:center;color:var(--white);
  font-family:"Crimson Text",serif;font-size:33px;line-height:40px}
.crumb{left:0;width:714px;top:243px;text-align:center;color:var(--white);font-size:10px}

/* Contact section */
.section-title{left:0;width:714px;top:364px;text-align:center;color:var(--ink);
  font-family:"Crimson Text",serif;font-size:31px;line-height:38px}
.field{left:52px;width:297px;border:1px solid var(--line);background:var(--white)}
.field .icon{position:absolute;left:0;top:0;width:24px;height:25px;border-right:1px solid var(--line);
  display:flex;align-items:center;justify-content:center}
.field .ph{position:absolute;left:32px;top:8px;font-size:7px;color:var(--muted)}
.send{left:52px;top:617px;width:80px;height:26px;background:var(--green);color:var(--white);
  font-size:7.5px;font-weight:500;text-align:center;line-height:26px}
.details{left:367px;top:426px;width:293px;height:217px;background:var(--green);color:var(--white)}
.details h3{position:absolute;left:45px;top:49px;font-weight:300;font-size:18px}
.details .row{position:absolute;left:45px;display:flex;font-size:8px;line-height:14px}
.details .dot{width:16px;height:16px;border-radius:50%;background:var(--green-soft);
  display:flex;align-items:center;justify-content:center;margin-right:12px;flex:none;margin-top:-1px}

/* Map */
.map{left:0;top:704px;width:714px;height:266px;background:linear-gradient(135deg,#ececec,#dcdcdc)}

/* Footer */
.footer{left:0;top:970px;width:714px;height:198px;background:var(--footer);color:var(--white)}
.footer h4{position:absolute;top:55px;font-family:"Crimson Text",serif;font-size:15px}
.footer p{position:absolute;font-size:7px;line-height:13px}
.links{position:absolute;left:341px;top:84px;list-style:none;font-size:7px}
.links li{height:20px}
.links li::before{content:"›";color:var(--muted);margin-right:6px}
.social{position:absolute;left:493px;top:112px;display:flex;gap:7px}
.social span{width:15px;height:15px;border-radius:50%;background:#1e1e1e}
.bottom{left:0;top:1168px;width:714px;height:32px;background:var(--footer-bottom);
  color:var(--white);font-size:7px;text-align:center;line-height:20px}
.totop{left:676px;top:1156px;width:20px;height:20px;border-radius:50%;background:var(--green);
  display:flex;align-items:center;justify-content:center}
</style>
</head>
<body>

<header>
  <div class="abs hero" role="img" aria-label="Photograph of a luxury stucco villa with a tiled roof, garage and palm trees under a blue sky"></div>
  <div class="abs hero-shade"></div>
  <div class="abs brand">KORA</div>
  <nav class="nav">
    <a style="left:434px">Home</a>
    <a style="left:474px">About Us</a>
    <a style="left:526px">Projects</a>
    <a class="btn">Contact Us</a>
  </nav>
  <svg class="abs burger" width="12" height="10" viewBox="0 0 12 10"><path d="M0 1h12M0 5h12M0 9h12" stroke="#fff" stroke-width="1.2"/></svg>
  <h1 class="abs hero-title">Contact Us</h1>
  <div class="abs crumb">Home / Contact Us</div>
</header>

<main>
  <h2 class="abs section-title">Get in touch</h2>

  <div class="abs field" style="top:426px;height:25px">
    <div class="icon"><svg width="8" height="8" viewBox="0 0 8 8"><circle cx="4" cy="2.3" r="2" fill="#777"/><path d="M0 8c0-3 8-3 8 0z" fill="#777"/></svg></div>
    <span class="ph">Name*</span>
  </div>
  <div class="abs field" style="top:455px;height:26px">
    <div class="icon"><svg width="8" height="6" viewBox="0 0 8 6"><rect width="8" height="6" fill="#777"/><path d="M0 0l4 3 4-3" stroke="#fff" stroke-width=".8" fill="none"/></svg></div>
    <span class="ph">Email*</span>
  </div>
  <div class="abs field" style="top:485px;height:25px">
    <div class="icon"><svg width="8" height="8" viewBox="0 0 8 8"><path d="M1 0l2 2-1 1.3c.8 1.4 1.5 2 2.7 2.7L6 5l2 2-1.2 1C3.5 7.5.5 4.5 0 1.2z" fill="#777"/></svg></div>
    <span class="ph">Phone*</span>
  </div>
  <div class="abs field" style="top:516px;height:93px">
    <div class="icon" style="height:93px;align-items:flex-start;padding-top:8px;border-right:none"><svg width="7" height="9" viewBox="0 0 7 9"><path d="M.5.5h4l2 2v6h-6z" stroke="#777" fill="none"/><path d="M2 4.5h3M2 6.5h3" stroke="#777" stroke-width=".7"/></svg></div>
    <span class="ph">Details*</span>
  </div>
  <div class="abs send">Send Details</div>

  <section class="abs details">
    <h3>Contact Details</h3>
    <div class="row" style="top:89px">
      <span class="dot"><svg width="6" height="8" viewBox="0 0 6 8"><path d="M3 8C1 5 0 4 0 3a3 3 0 016 0c0 1-1 2-3 5z" fill="#fff"/><circle cx="3" cy="3" r="1" fill="#8cc866"/></svg></span>
      <span>Stonefield House, 42 Quarry Lane, Harrowgate<br>HG4 2TR</span>
    </div>
    <div class="row" style="top:126px">
      <span class="dot"><svg width="7" height="7" viewBox="0 0 8 8"><path d="M1 0l2 2-1 1.3c.8 1.4 1.5 2 2.7 2.7L6 5l2 2-1.2 1C3.5 7.5.5 4.5 0 1.2z" fill="#fff"/></svg></span>
      <span>+44 (0) 100 555 0148</span>
    </div>
    <div class="row" style="top:149px">
      <span class="dot"><svg width="7" height="5" viewBox="0 0 8 6"><rect width="8" height="6" fill="#fff"/><path d="M0 0l4 3 4-3" stroke="#8cc866" stroke-width=".8" fill="none"/></svg></span>
      <span>hello@korastudio.example</span>
    </div>
  </section>

  <div class="abs map" role="img" aria-label="Street map of the studio's neighbourhood with a location marker"></div>
</main>

<footer>
  <div class="abs footer">
    <h4 style="left:51px">About Us</h4>
    <p style="left:52px;top:86px;width:222px">Sed ac mauris sit amet ante. Maecenas eu nibh. Aliquam fermen-tum eget, suscipit congue id, lacinia accumsan lectus nec lectus lectus, luctus et ultrices metus imperdiet facilisis est eu quam. Phasellus ut ante donec mi.</p>
    <h4 style="left:341px">Useful Links</h4>
    <ul class="links"><li>Home</li><li>About Us</li><li>Projects</li><li>Contact Us</li></ul>
    <h4 style="left:492px">Contact</h4>
    <p style="left:493px;top:84px;width:150px;line-height:10px">Duis dictum eleifend tortor at scelerisque Sed elementum augue eu.</p>
    <div class="social"><span></span><span></span><span></span><span></span><span></span></div>
    <p style="left:493px;top:135px;line-height:12px">Contact us: +61 (0) 3 5550 0172<br>Write us: info@korastudio.example</p>
  </div>
  <div class="abs bottom">Copyright@2017 | All right Reserved</div>
  <div class="abs totop"><svg width="6" height="4" viewBox="0 0 6 4"><path d="M.5 3.5L3 1l2.5 2.5" stroke="#fff" fill="none"/></svg></div>
</footer>

</body>
</html>
```